Als Manufaktur einzigartiger Fachmedien präsentiert verlag-kontor Schlüsseltechnologien und ihre Märkte. Faszination für Technik ist die Grundlage unserer Arbeit. Mehr als 30 Jahre verlegerische Erfahrung und das Verständnis für Technologiemärkte machen uns zu einem anerkannten Partner der Industrie.
Unsere Medienmarken knüpfen ein starkes und weit verzweigtes Netzwerk – Print und digital – , in dem sich Anbieter und Anwender von Technologien und Produkten in ihren Zielsetzungen wiederfinden.
Unsere Magazine, Events und Netzwerkveranstaltungen sowie kundenspezifische Kommunikations- & Strategiekampagnen setzen in ihren Zielmärkten Maßstäbe und genießen bei Lesern, Kunden und Partnern Vertrauen und Respekt.
Für das ausgeschriebene Projekt handelt es sich um unsere Referenzpublikation SECTOR.ahead MORILUNA.
MORILUNA {polynesisch: Freiraum}
Das Referenzbuch der Industrie. Für Vorwärtsdenker und Zukunftsmacher.
Wandel bestimmt unsere Zeit und verändert unsere Gesellschaft, unsere Unternehmen, uns alle.
Im Wandel liegt Freiraum zur Gestaltung. Gesellschaftlicher Wandel, Technologie-Wandel, Klimawandel, Wertewandel, Führungswandel oder Organisationswandel sind nur einige Beispiele. Wer dabei den Wandel in engen Bahnen denkt, verschenkt Potential. Veränderung braucht Freiraum für neue Ideen und Perspektiven sowie Persönlichkeiten, die diesen nutzen wollen.
Aber wer gestaltet die Zukunft der Industrie und ihrer Branchen? Und wie?
Wir geben Personen aus der Industrie den Freiraum, ihre Perspektiven auf und aus dem Wandel zu erzählen. Warum? Weil sie uns begeistert haben, in persönlichen Treffen und Gesprächen, durch streitbare Meinungen und ehrliche Geschichten. Weil sie die Zukunft verändern.
MORILUNA ist eine Aufforderung: Zum Mitdenken, Weiterdenken, aber auch Nachdenken.
MORILUNA – FREIRAUM FÜR IDEEN
Ein Referenzbuch, d..
1. Kurzzusammenfassung der Ausschreibung
Die 4. Ausgabe des jährlichen Referenzbuchs der Industrie, SECTOR.ahead MORILUNA 2025, erscheint im Oktober 2024. Für das Cover sucht der verlag-kontor Verlag neue Vorschläge, die die Themen Freiraum und Wandel in den Fokus stellen.
2. Gestalterische & Inhaltliche Anforderungen
• Format: 195x250 mm + Anschnitt
• Rücken: ca. 1,6 cm (Stand letzte Publikation 2023)
• Auflösung: Druckqualität, mind. 300 dpi
• Inhaltliche Elemente:
- MORILUNA Schriftzug
- {polynesisch: Freiraum}
- Untersatz: Das Referenzbuch der Industrie. Für Vorwärtsdenker und Zukunftsmacher.
- part of SECTOR.ahead Logo-Balken am unteren Rand (siehe Beispiel AuD_Titelbeispiel_Logobalken)
WICHTIG: Der aktuelle Schriftzug MORILUNA und die Farbe Orange (0/80/100/0) (siehe Beispiel MORILUNA 2021) sollen als Wiedererkennung in die Gestaltungen eingebunden werden.

```html
<!DOCTYPE html>
<html lang="de">
<head>
<meta charset="utf-8">
<title>MORILUNA 2024 – Cover</title>
<link rel="stylesheet" href="https://fonts.googleapis.com/css2?family=Anton&family=Bebas+Neue&family=Krona+One&family=Oswald:wght@300&display=swap">
<style>
  :root {
    --orange: #ea4f24;
    --orange-tint: #f7c9b8;
    --white: #ffffff;
    --ink: #1d1d1b;
    --stage: #d2d2d2;
  }
  html, body {
    margin: 0;
    padding: 0;
    overflow: hidden;
  }
  body {
    width: 1200px;
    height: 2317px;
    background: var(--stage);
    position: relative;
  }
  .cover {
    position: absolute;
    left: 100px;
    top: 518px;
    width: 1000px;
    height: 1281px;
    box-shadow: 6px 8px 14px rgba(0, 0, 0, 0.25);
    background: var(--white);
  }
  .cover svg { display: block; }
  .wordmark {
    font-family: "Anton", "Bebas Neue", sans-serif;
    fill: var(--white);
  }
  .translation {
    font-family: "Oswald", sans-serif;
    font-weight: 300;
    fill: var(--white);
  }
  .edition-year {
    font-family: "Krona One", sans-serif;
    fill: var(--orange);
  }
  .tagline {
    font-family: "Bebas Neue", "Oswald", sans-serif;
    fill: var(--ink);
  }
  .series-bar {
    font-family: "Bebas Neue", "Oswald", sans-serif;
    fill: var(--white);
  }
  .series-bar .part-of {
    font-family: "Oswald", sans-serif;
    font-weight: 300;
  }
</style>
</head>
<body>
  <div class="cover">
    <svg width="1000" height="1281" viewBox="0 0 1000 1281" xmlns="http://www.w3.org/2000/svg">
      <defs>
        <clipPath id="cover-clip"><rect width="1000" height="1281"/></clipPath>
      </defs>
      <g clip-path="url(#cover-clip)">
        <rect class="paper" width="1000" height="1281" fill="var(--white)"/>

        <rect class="climber-illustration" x="590" y="660" width="280" height="400" rx="6" fill="var(--orange-tint)"
          role="img" aria-label="Illustration: Geschäftsmann mit Aktentasche steigt die Treppe hinauf"/>

        <polygon class="column-and-stairs" fill="var(--orange)"
          points="0,0 387,0 387,822 507,822 507,891 598,891 598,964 694,964 694,1041 786,1041 786,1114 895,1114 895,1187 1000,1187 1000,1281 0,1281"/>

        <g class="wordmark">
          <text x="-28" y="296" font-size="370" textLength="370" lengthAdjust="spacingAndGlyphs">MO</text>
          <text x="-28" y="610" font-size="370" textLength="370" lengthAdjust="spacingAndGlyphs">RI</text>
          <text x="-28" y="967" font-size="370" textLength="370" lengthAdjust="spacingAndGlyphs">LU</text>
          <text x="-28" y="1281" font-size="370" textLength="370" lengthAdjust="spacingAndGlyphs">NA</text>
        </g>

        <text class="translation" x="74" y="648" font-size="19">{polynesisch: Freiraum}</text>

        <text class="edition-year" x="474" y="354" font-size="80" textLength="372" lengthAdjust="spacingAndGlyphs">2024</text>

        <g class="tagline" font-size="46">
          <text x="471" y="464" textLength="449" lengthAdjust="spacingAndGlyphs">DAS REFERENZBUCH DER INDUSTRIE.</text>
          <text x="471" y="514" textLength="348" lengthAdjust="spacingAndGlyphs">FÜR VORWÄRTSDENKER UND</text>
          <text x="471" y="563" textLength="240" lengthAdjust="spacingAndGlyphs">ZUKUNFTSMACHER.</text>
        </g>

        <g class="series-bar">
          <text class="part-of" x="538" y="1178" font-size="20">part of</text>
          <text x="597" y="1178" font-size="47" textLength="276" lengthAdjust="spacingAndGlyphs">SECTOR.AHEAD</text>
        </g>
      </g>
    </svg>
  </div>
</body>
</html>
```